Business Card - Rebranding for Consulting Firm

We are renaming and rebranding our consulting firm and need to raise the level of quality of our cards as part of that effort. We consult to leading high tech, life science and other innovation sector companies.

Need a two-sided business card design.

Side 1: (a) Company logo (b) tag line: Optimize Your Investment in Talent (c) Name (d) Title (e) Phone 1: Office (f) Phone 2: Mobile (g) email: person@HollowmereAdvisory.com

Side 2: Two lines of text: (a) Growth is Imperative. Change is Constant. Talent Executes Strategy. (b) We help you excel at all three.

Target Market(s)

Business and human resources executives and senior managers

Industry/Entity Type

Management Consulting

Contact Information for Business Card

Font styles to use
Sans Serif

Requirements
Must have
• clean, not too busy, but with a bit of creativity. Stick to the colors used in the attached logo
• appeal to high tech, life science companies
Nice to have
• prefer white background

```html
<!DOCTYPE html>
<html lang="en">
<head>
<meta charset="utf-8">
<title>Hollowmere Advisory – Business Card</title>
<link href="https://fonts.googleapis.com/css2?family=Source+Sans+3:wght@400;600&display=swap" rel="stylesheet">
<style>
  :root {
    --backdrop: #262626;
    --card-white: #ffffff;
    --brand-blue: #0c69a3;
    --ink: #3a3a3a;
    --muted: #7a7a7a;
    --reverse-grey: #828282;
    --reverse-text: #ffffff;
  }
  * { box-sizing: border-box; margin: 0; padding: 0; }
  html, body {
    width: 1200px; height: 987px; overflow: hidden;
    background: var(--backdrop);
    font-family: "Source Sans 3", sans-serif;
  }
  .stage { position: relative; width: 1200px; height: 987px; }

  .card {
    position: absolute; left: 293px; width: 615px; height: 352px; overflow: hidden;
  }
  .card--front { top: 130px; background: var(--card-white); }
  .card--back { top: 505px; background: var(--reverse-grey); }

  .brand {
    display: flex; align-items: center; gap: 10px;
  }
  .brand__mark { width: 22px; height: 22px; flex: none; }
  .brand__name {
    font-weight: 600; font-size: 36px; letter-spacing: -0.5px; line-height: 1;
  }
  .card--front .brand { position: absolute; left: 31px; top: 66px; }
  .card--front .brand__mark { background: var(--brand-blue); }
  .card--front .brand__name { color: var(--brand-blue); }

  .contact-list {
    position: absolute; left: 31px; top: 196px; list-style: none;
  }
  .contact-list li {
    display: flex; align-items: center; gap: 6px;
    height: 23.5px; font-size: 16px; color: var(--ink);
  }
  .contact-list svg { width: 16px; height: 16px; fill: var(--brand-blue); flex: none; }

  .person {
    position: absolute; right: 31px; top: 244px; text-align: right;
  }
  .person__name { font-size: 21px; font-weight: 600; color: var(--brand-blue); line-height: 1.1; }
  .person__title { font-size: 16px; color: var(--muted); line-height: 1.4; }

  .tagline-band {
    position: absolute; left: 0; right: 0; bottom: 0; height: 39px;
    background: var(--brand-blue); color: var(--reverse-text);
    display: flex; align-items: center; justify-content: center;
    font-size: 16px; font-weight: 600;
  }

  .card--back .brand {
    position: absolute; left: 0; right: 0; top: 152px; justify-content: center;
  }
  .card--back .brand__mark { background: var(--reverse-text); }
  .card--back .brand__name { color: var(--reverse-text); font-size: 44px; }

  .manifesto {
    position: absolute; left: 0; right: 0; top: 276px;
    text-align: center; color: var(--reverse-text); font-size: 16px; line-height: 1.45;
  }
</style>
</head>
<body>
<div class="stage">
  <section class="card card--front" aria-label="Business card front">
    <div class="brand">
      <span class="brand__mark"></span>
      <span class="brand__name">Hollowmere Advisory</span>
    </div>

    <ul class="contact-list">
      <li>
        <svg viewBox="0 0 16 16" aria-hidden="true"><path d="M3 2h3l1.5 3.5-2 1.3a8 8 0 0 0 3.7 3.7l1.3-2L14 10v3a1 1 0 0 1-1 1A11 11 0 0 1 2 3a1 1 0 0 1 1-1z"/></svg>
        555 0147 2290
      </li>
      <li>
        <svg viewBox="0 0 16 16" aria-hidden="true"><path d="M4.5 1h7a1 1 0 0 1 1 1v12a1 1 0 0 1-1 1h-7a1 1 0 0 1-1-1V2a1 1 0 0 1 1-1zm.8 2v9h5.4V3zM8 12.6a.8.8 0 1 0 0 1.6.8.8 0 0 0 0-1.6z"/></svg>
        555 0183 6614
      </li>
      <li>
        <svg viewBox="0 0 16 16" aria-hidden="true"><path d="M1 4h14v1L8 9.5 1 5zm0 2.3 7 4.5 7-4.5V12H1z"/></svg>
        person@HollowmereAdvisory.com
      </li>
      <li>
        <svg viewBox="0 0 16 16" aria-hidden="true"><circle cx="8" cy="8" r="6.5"/></svg>
        www.HollowmereAdvisory.com
      </li>
    </ul>

    <div class="person">
      <p class="person__name">Marcus Hale</p>
      <p class="person__title">President</p>
    </div>

    <div class="tagline-band">Optimize Your Investment in Talent</div>
  </section>

  <section class="card card--back" aria-label="Business card back">
    <div class="brand">
      <span class="brand__mark"></span>
      <span class="brand__name">Hollowmere Advisory</span>
    </div>
    <p class="manifesto">
      Growth is Imperative. Change is Constant. Talent Executes Strategy.<br>
      We help you excel at all three.
    </p>
  </section>
</div>
</body>
</html>
```